TV+Music+Social Network+Entertainment+brightlistin= Designers lol

TV+ Music+ Social Network +Entertainment+ brightlistin=

ZELLOPAK.COM

Zellopak is a one-stop shop promotional plateform that will communicate information to all user of what is COOL, NEW and Exicting in your Neighborhood.(News,Events,Entertainment,ect) We promote for all User/Entrepreneur/business/Talents.We are the future and dream destination for all to whom owns a computer. Forming the the World Wide Web into your Local Wide Web. (Atlanta, Dallas, Las Vegas, New York ect.)

* EX: ( WWW. ??? .com =LWW. ??? .com)
WORLD = LOCAL

* Goal/Mission: Have customer/user visit the website and then leave their house to go experience life in their respective surroundings.

/////////////////////////Web page///////////////////////

Colors:Blue/Green/black

include: interchangable background picture @ top (to update easily and keep fresh) On this background picture include logo (top left) login/sign (top left)

Major Tabs: Music/Daylife/Nightlife/Video/Shop

Industry/Entity Type

House

Requirements
Nice to have
• Tv screen/search engine

```html
<!DOCTYPE html>
<html lang="en">
<head>
<meta charset="utf-8">
<title>Zellopak – Your Local Wide Web</title>
<link rel="stylesheet" href="https://fonts.googleapis.com/css2?family=Arimo:wght@400;700&family=Gelasio:wght@400;700&display=swap">
<style>
:root{
  --sky-deep:#0b4f8f;
  --sky:#1f86c9;
  --sky-light:#7fd0f2;
  --navy:#0d2a6b;
  --navy-dark:#1b2433;
  --link:#1a6fb5;
  --heading-blue:#1f5fae;
  --green:#4f8a12;
  --green-light:#7fbf2a;
  --text:#3b3b3b;
  --muted:#777;
  --band:#e2dfd9;
  --card-border:#d6d3cc;
  --footer:#0a1922;
  --footer-line:#22343f;
  --footer-text:#c7d3da;
  --accent-yellow:#f2c21a;
  --white:#fff;
}
*{box-sizing:border-box;margin:0;padding:0}
html,body{width:798px;height:1200px;overflow:hidden;background:var(--white)}
body{font-family:"Arimo",Arial,sans-serif;color:var(--text);font-size:9px}
.page{position:relative;width:798px;height:1200px;overflow:hidden}
.abs{position:absolute}
.serif{font-family:"Gelasio",Georgia,serif}

/* header */
.header-bg{position:absolute;left:0;top:0;width:798px;height:300px}
.login-bar{left:440px;top:2px;width:265px;height:21px;background:rgba(255,255,255,.9);clip-path:polygon(0 0,100% 0,97% 100%,0 100%)}
.login-tab{left:350px;top:2px;width:92px;height:22px;background:linear-gradient(var(--green-light),var(--green));color:var(--white);font-size:13px;letter-spacing:.5px;display:flex;align-items:center;justify-content:center;clip-path:polygon(8% 0,100% 0,100% 100%,0 100%)}
.field{height:18px;border-radius:9px;background:var(--white);border:1px solid #cfd8de;font-size:9px;color:#333;padding-left:10px;display:flex;align-items:center}
.go-btn{left:661px;top:4px;width:31px;height:18px;border-radius:9px;background:linear-gradient(#2d7fd0,#0d3f86);color:var(--white);font-size:9px;font-weight:700;display:flex;align-items:center;justify-content:center}
.search-box{left:379px;top:37px;width:287px;height:30px;border-radius:15px;background:rgba(255,255,255,.55);border:1px solid rgba(255,255,255,.8)}
.search-input{left:384px;top:41px;width:158px;height:22px;border-radius:11px 0 0 11px;background:var(--white);font-size:9px;color:#333;padding-left:9px;display:flex;align-items:center}
.city-select{left:542px;top:41px;width:62px;height:22px;background:#eef1f3;font-size:9px;font-weight:700;color:#333;display:flex;align-items:center;padding-left:6px;border-left:1px solid #ccc}
.search-btn{left:605px;top:42px;width:56px;height:20px;border-radius:10px;background:linear-gradient(#3b8fe0,#0a3d88);color:var(--white);font-size:9px;font-weight:700;display:flex;align-items:center;justify-content:center;letter-spacing:.5px}
.advance{left:541px;top:66px;width:79px;height:15px;background:var(--white);color:var(--link);font-size:9px;display:flex;align-items:center;justify-content:center}
.logo-plate{left:62px;top:40px;width:226px;height:90px}
.logo-name{left:104px;top:78px;color:var(--white);font-size:20px;font-weight:700;display:flex;align-items:center;gap:7px}
.logo-dot{width:26px;height:26px;border-radius:50%;background:var(--sky)}
.tab{top:93px;height:34px;color:var(--white);font-size:13px;letter-spacing:.8px;display:flex;align-items:center;justify-content:center;clip-path:polygon(10% 0,90% 0,100% 100%,0 100%)}
.tab.music{left:310px;width:86px;background:#1b2634}
.tab.daylife{left:386px;width:88px;background:#2c3b4d}
.tab.nightlife{left:464px;width:90px;background:#1f2c3c}
.tab.video{left:544px;width:88px;background:#6f8392}
.tab.shop{left:620px;width:84px;background:#b1bfc8}

/* slider */
.slider-shadow{left:120px;top:372px;width:560px;height:22px;background:radial-gradient(ellipse at 50% 0,rgba(0,0,0,.28),rgba(0,0,0,0) 70%)}
.slider{left:93px;top:126px;width:611px;height:251px;background:var(--navy);padding:5px}
.slider-inner{position:relative;width:100%;height:100%;background:var(--white)}
.slide-photo{left:2px;top:2px;width:275px;height:236px;background:linear-gradient(180deg,#fbfbfb,#ecedef)}
.slide-title{left:302px;top:37px;font-size:20px;color:#333}
.slide-copy{left:302px;top:60px;width:275px;font-size:9px;line-height:12px;color:#444}
.dotted{border-top:1px dotted #b9b9b9;width:275px;left:302px}
.service-label{left:302px;top:108px;font-size:9.5px;color:#333}
.service-links{left:302px;top:121px;font-size:8.5px;color:var(--link)}
.select-city{left:303px;top:152px;width:76px;height:18px;border-radius:9px;background:linear-gradient(#79b22b,#3c6f0c);color:var(--white);font-size:8.5px;display:flex;align-items:center;justify-content:center}
.stats-banner{left:232px;top:202px;width:367px;height:36px;background:linear-gradient(90deg,#2aa7e6,#0e74c6);clip-path:polygon(5% 0,100% 0,100% 100%,0 100%);color:var(--white);font-weight:700}
.stat{position:absolute;line-height:1}
.stat b{display:block;font-size:15px}
.stat span{font-size:8px}
.slide-arrow{top:116px;width:14px;height:14px;border-radius:50%;background:#1d5fae;border:1px solid #7fb0e0}

/* welcome */
.welcome-title{left:92px;top:405px;font-size:20px;color:var(--heading-blue)}
.welcome-copy{left:93px;top:437px;width:400px;font-size:9px;line-height:12.5px;color:#444}
.today-title{left:516px;top:406px;font-size:12px;color:#222}
.today-photo{left:517px;top:427px;width:94px;height:53px;background:linear-gradient(135deg,#3a2e2c,#a27f6c 55%,#d6c6b9)}
.today-link{left:619px;top:426px;font-size:8.5px;color:var(--link)}
.today-copy{left:619px;top:437px;width:90px;font-size:8.5px;line-height:11px;color:#555}
.bullet-list{list-style:none;font-size:8.5px;color:#444}
.bullet-list li{position:relative;padding-left:9px}
.bullet-list li::before{content:"›";position:absolute;left:0;color:#999}

/* columns */
.band{left:0;top:550px;width:798px;height:464px;background:var(--band);box-shadow:inset 0 6px 8px -6px rgba(0,0,0,.25)}
.col-title{top:572px;font-size:16px;color:#333}
.card{top:600px;width:199px;height:384px;background:var(--white);border:1px solid var(--card-border)}
.card-headline{left:0;top:9px;width:100%;text-align:center;font-size:15px;line-height:15px;color:#111;padding:0 14px}
.card-photo{left:12px;top:56px;width:173px;height:97px}
.card-date{left:0;top:163px;width:100%;text-align:center;font-size:8.5px;color:#666}
.card-copy{left:0;top:174px;width:100%;text-align:center;font-size:8.5px;line-height:12.5px;color:#444;padding:0 12px}
.read-more{left:62px;top:219px;width:75px;height:12px;background:var(--green);color:var(--white);font-size:7.5px;display:flex;align-items:center;justify-content:center;clip-path:polygon(6% 0,100% 0,94% 100%,0 100%)}
.card-sub{left:15px;top:246px;font-size:8.5px;font-weight:700;color:#222}
.card-list{left:15px;top:264px;width:170px;line-height:11px}
.card-list li{margin-bottom:6.5px}
.more-item{left:16px;width:170px;height:28px}
.more-thumb{position:absolute;left:0;top:0;width:51px;height:28px}
.more-link{position:absolute;left:58px;top:-2px;font-size:8px;line-height:10px;color:var(--link)}
.more-time{position:absolute;left:58px;top:19px;font-size:7px;color:#666}

/* footer */
.footer{left:0;top:1013px;width:798px;height:187px;background:radial-gradient(ellipse at 50% 40%,#10273a,var(--footer) 70%)}
.newsletter-label{left:96px;top:1032px;font-size:12px;color:var(--white)}
.newsletter-input{left:166px;top:1027px;width:157px;height:22px;border-radius:3px;background:linear-gradient(#fff,#d7d7d7);font-size:9px;color:#222;display:flex;align-items:center;padding-left:7px}
.subscribe{left:330px;top:1027px;width:70px;height:22px;border-radius:3px;background:linear-gradient(#8ccf32,#4c8a10);color:#111;font-size:11px;display:flex;align-items:center;justify-content:center}
.quote-icon{left:505px;top:1025px;width:26px;height:26px;border-radius:4px;background:#f08a1a}
.quote-text{left:538px;top:1024px;color:var(--white);font-size:11.5px;line-height:15px;letter-spacing:.3px}
.quote-text em{font-style:normal;color:var(--accent-yellow)}
.quote-text small{font-size:6.5px}
.rule{background:var(--footer-line);height:1px}
.cat{top:1067px;width:44px;text-align:center;color:var(--footer-text);font-size:9px}
.cat svg{display:block;margin:0 auto 2px}
.sub-site{top:1072px;font-size:11px;color:#3fa4e6;line-height:12px}
.sub-site span{display:block;font-size:8.5px;color:#9aa7ae}
.cities{left:93px;top:1120px;font-size:8px;line-height:13px;color:var(--footer-text)}
.promo{top:1106px;height:50px;border-left:1px solid var(--footer-line);color:var(--white);font-size:11px;line-height:11px;display:flex;align-items:center;padding-left:16px;gap:8px}
.promo::before{content:"";position:absolute;left:0;top:0;border-top:10px solid var(--green);border-right:10px solid transparent}
.social{top:1118px;width:24px;height:24px;border-radius:3px}
.legal{left:347px;top:1164px;font-size:7.5px;color:var(--footer-text);word-spacing:1px}
.copyright{left:590px;top:1180px;font-size:7.5px;color:#3fa4e6}
</style>
</head>
<body>
<div class="page">

  <!-- header background -->
  <svg class="header-bg" viewBox="0 0 798 300" aria-hidden="true">
    <defs>
      <radialGradient id="skyGlow" cx="0.5" cy="0.15" r="0.75">
        <stop offset="0" stop-color="#c8f0ff"/>
        <stop offset="0.35" stop-color="#3fa9e2"/>
        <stop offset="1" stop-color="#0a4b8a"/>
      </radialGradient>
    </defs>
    <path d="M0 0H798V292Q600 215 399 212Q200 215 0 292Z" fill="url(#skyGlow)"/>
  </svg>

  <!-- login -->
  <div class="abs login-bar"></div>
  <div class="abs login-tab">LOGIN IN</div>
  <div class="abs field" style="left:447px;top:3px;width:102px">Username</div>
  <div class="abs field" style="left:554px;top:3px;width:104px">Password</div>
  <div class="abs go-btn">GO</div>

  <!-- search -->
  <div class="abs search-box"></div>
  <div class="abs search-input">I am looking for</div>
  <div class="abs city-select">ATLANTA&nbsp;<span style="color:#888">▾</span></div>
  <div class="abs search-btn">SEARCH</div>
  <div class="abs advance">Advance search</div>

  <!-- logo -->
  <svg class="abs logo-plate" viewBox="0 0 226 90" aria-hidden="true">
    <path d="M18 2H168Q182 2 190 14L224 88H4Q0 88 2 80L4 18Q6 2 18 2Z" fill="#7bb52c"/>
    <path d="M16 6H162Q174 6 181 17L214 88H6L6 20Q6 6 16 6Z" fill="#0d0f12"/>
  </svg>
  <div class="abs logo-name"><span class="logo-dot"></span>zellopak</div>

  <!-- tabs -->
  <nav>
    <div class="abs tab shop">SHOP</div>
    <div class="abs tab video">VIDEO</div>
    <div class="abs tab nightlife">NIGHTLIFE</div>
    <div class="abs tab daylife">DAYLIFE</div>
    <div class="abs tab music">MUSIC</div>
  </nav>

  <!-- slider -->
  <div class="abs slider-shadow"></div>
  <section class="abs slider">
    <div class="slider-inner">
      <div class="abs slide-photo" role="img" aria-label="Four-piece rock band performing with guitars, drums and microphone"></div>
      <h2 class="abs slide-title serif" style="font-weight:400">Music Event Organisers</h2>
      <p class="abs slide-copy">Lorem ipsum dolor sit 13000 amet, consectetur adipisicing elit, sed do eiusmod tempor incididunt ut labore et dolore magna aliqua. Ut enim ad minim veniam,</p>
      <div class="abs dotted" style="top:99px"></div>
      <div class="abs service-label">Service Types</div>
      <div class="abs service-links">Classical music &nbsp;<span style="color:#999">|</span>&nbsp; Rock music</div>
      <div class="abs dotted" style="top:140px"></div>
      <div class="abs select-city">SELECT CITY</div>
      <div class="abs stats-banner">
        <div class="stat" style="left:26px;top:6px"><b>25+YEARS OF EXPERIENCE</b><span>IN CONNECTING CUSTOMERS TO SUPPLIERS</span></div>
        <div class="stat" style="left:243px;top:6px"><b>250+</b><span>CITIES</span></div>
        <div class="stat" style="left:293px;top:6px"><b>50,000+</b><span>SUPPLIERS</span></div>
      </div>
    </div>
  </section>
  <div class="abs slide-arrow" style="left:95px;top:244px"></div>
  <div class="abs slide-arrow" style="left:688px;top:244px"></div>

  <!-- welcome -->
  <h1 class="abs welcome-title serif" style="font-weight:400">Welcome to Zellopak</h1>
  <p class="abs welcome-copy">Lorem ipsum dolor sit amet, consectetur adipisicing elit, sed do eiusmod tempor incididunt ut labore et dolore magna aliqua. Ut enim ad minim veniam, quis nostrud exercitation ullamco laboris nisi ut aliquip ex ea commodo consequat. Duis aute irure dolor in reprehenderit in voluptate velit esse cillum dolore eu fugiat nulla pariatur. Excepteur sint occaecat cupidatat non proident, sunt in culpa qui officia deserunt mollit anim id est laborum.</p>

  <h3 class="abs today-title serif" style="font-weight:400">Today on Zellopak News</h3>
  <div class="abs today-photo" role="img" aria-label="Celebrity in a wide hat and sunglasses on the red carpet"></div>
  <div class="abs today-link">Red Carpet Wrap</div>
  <p class="abs today-copy">50 Pictures: Hollywood starlets show off unique fashion choices.</p>
  <ul class="abs bullet-list" style="left:517px;top:489px;line-height:13.5px">
    <li>Sed sit amet purus nisl, hendrerit pulvinar urna.</li>
    <li>Ut ac lorem mauris, id semper tellus.</li>
    <li>Curabitur ultricies velit in nulla iaculis ultrices.</li>
  </ul>

  <!-- columns -->
  <div class="abs band"></div>
  <h3 class="abs col-title serif" style="left:93px;font-weight:400">Latest News</h3>
  <h3 class="abs col-title serif" style="left:298px;font-weight:400">Events</h3>
  <h3 class="abs col-title serif" style="left:504px;font-weight:400">Entertainment</h3>

  <article class="abs card" style="left:93px">
    <h4 class="abs card-headline serif" style="font-weight:400">Lorem ipsum dolor sit commodo duis</h4>
    <div class="abs card-photo" role="img" aria-label="Guitarist in a hat playing acoustic guitar on a dark stage" style="background:linear-gradient(135deg,#1a1412,#5a3a26 55%,#20160f)"></div>
    <div class="abs card-date serif">30/4/2012, Apr</div>
    <p class="abs card-copy">Lorem ipsum dolor sit amet, consectetur adipisicing elit, sed do eiusmod tempor incididunt ut labore et dolore magna aliqua.</p>
    <div class="abs read-more">READ MORE</div>
    <div class="abs card-sub">More Headlines</div>
    <ul class="abs bullet-list card-list">
      <li>Sed sit amet purus nisl, hendrerit pulvinar urna.</li>
      <li>Ut ac lorem mauris, id semper tellus.</li>
      <li>Curabitur ultricies velit in nulla iaculis ultrices.</li>
      <li>Aenean sit amet velit ut mi pretium ultrices.</li>
      <li>Donec mattis mi et ligula luctus vulputate.</li>
    </ul>
  </article>

  <article class="abs card" style="left:298px">
    <h4 class="abs card-headline serif" style="font-weight:400">Ultricies velit in nulla iaculis ultrices.</h4>
    <div class="abs card-photo" role="img" aria-label="Smiling man in a yellow shirt at an outdoor event" style="background:linear-gradient(135deg,#b9c7a0,#e7d36a 50%,#8aa160)"></div>
    <div class="abs card-date serif">30/4/2012, Apr</div>
    <p class="abs card-copy">Lorem ipsum dolor sit amet, consectetur adipisicing elit, sed do eiusmod tempor incididunt ut labore et dolore magna aliqua.</p>
    <div class="abs read-more">READ MORE</div>
    <div class="abs card-sub">More Events</div>
    <ul class="abs bullet-list card-list">
      <li>Sed sit amet purus nisl, hendrerit pulvinar urna.</li>
      <li>Ut ac lorem mauris, id semper tellus.</li>
      <li>Curabitur ultricies velit in nulla iaculis ultrices.</li>
      <li>Aenean sit amet velit ut mi pretium ultrices.</li>
      <li>Donec mattis mi et ligula luctus vulputate.</li>
    </ul>
  </article>

  <article class="abs card" style="left:504px">
    <h4 class="abs card-headline serif" style="font-weight:400">Canuck cast savouring Rory nods for 'Superstar'</h4>
    <div class="abs card-photo" role="img" aria-label="Video still of a stage musical performance under blue lights" style="background:linear-gradient(180deg,#1c3f8a,#3b6fc4 50%,#0e1e44)"></div>
    <div class="abs card-date serif">2/5/2012, May</div>
    <p class="abs card-copy">Lorem ipsum dolor sit amet, consectetur adipisicing elit, sed do eiusmod tempor incididunt ut labore et dolore magna aliqua.</p>
    <div class="abs read-more">READ MORE</div>
    <div class="abs card-sub">More</div>
    <div class="abs more-item" style="top:262px">
      <div class="more-thumb" role="img" aria-label="Group of starlets on the red carpet" style="background:linear-gradient(90deg,#6b4a3c,#c99c82)"></div>
      <div class="more-link">Red Carpet Wrap: Starlets<br>show off unique, chic looks</div>
      <div class="more-time">Thursday May. 3 6:59 AM</div>
    </div>
    <div class="abs more-item" style="top:298px">
      <div class="more-thumb" role="img" aria-label="Pop singer portrait" style="background:linear-gradient(90deg,#2a2230,#6a5a70)"></div>
      <div class="more-link">Korean pop star to kick off tour<br>with high-fives</div>
      <div class="more-time">Thursday May. 3 7:08 AM</div>
    </div>
    <div class="abs more-item" style="top:335px">
      <div class="more-thumb" role="img" aria-label="Film still of an actor in a dark scene" style="background:linear-gradient(90deg,#3d3a2a,#8a8060)"></div>
      <div class="more-link">Marcus Delane goes<br>full-fledged Captain Vance</div>
      <div class="more-time">Wednesday May. 2 11:05 AM ET</div>
    </div>
  </article>

  <!-- footer -->
  <footer class="abs footer"></footer>
  <div class="abs newsletter-label">Newsletter</div>
  <div class="abs newsletter-input">Enter your email</div>
  <div class="abs subscribe">Subscribe</div>
  <div class="abs quote-icon"></div>
  <div class="abs quote-text">QUERIES OR FREE QUOTES<br>CALL <em>1900-555-0142</em> <small>(TOLL FREE)</small></div>
  <div class="abs rule" style="left:93px;top:1062px;width:611px"></div>

  <div class="abs cat" style="left:86px">
    <svg width="20" height="20" viewBox="0 0 20 20" aria-hidden="true"><path d="M3 12a7 7 0 0 1 14 0" fill="none" stroke="#cfd6db" stroke-width="2"/><rect x="2" y="11" width="4" height="7" rx="1" fill="#cfd6db"/><rect x="14" y="11" width="4" height="7" rx="1" fill="#cfd6db"/></svg>Music</div>
  <div class="abs cat" style="left:143px">
    <svg width="20" height="20" viewBox="0 0 20 20" aria-hidden="true"><circle cx="10" cy="10" r="5" fill="#f2b51a"/><g stroke="#f2b51a" stroke-width="1.5"><path d="M10 1v3M10 16v3M1 10h3M16 10h3M4 4l2 2M14 14l2 2M4 16l2-2M14 6l2-2"/></g></svg>Daylife</div>
  <div class="abs cat" style="left:207px">
    <svg width="20" height="20" viewBox="0 0 20 20" aria-hidden="true"><circle cx="10" cy="10" r="8" fill="#1f3c55"/><circle cx="13" cy="8" r="6" fill="#0f2534"/></svg>Nightlife</div>
  <div class="abs cat" style="left:269px">
    <svg width="24" height="20" viewBox="0 0 24 20" aria-hidden="true"><rect x="2" y="6" width="15" height="11" rx="2" fill="#cfd6db"/><path d="M17 10l5-3v10l-5-3z" fill="#cfd6db"/><circle cx="6" cy="4" r="3" fill="#9aa7ae"/><circle cx="12" cy="4" r="3" fill="#9aa7ae"/></svg>Video</div>
  <div class="abs cat" style="left:324px">
    <svg width="22" height="20" viewBox="0 0 22 20" aria-hidden="true"><path d="M6 7a5 5 0 0 1 10 0" fill="none" stroke="#7cc0ea" stroke-width="1.5"/><path d="M2 7h18l-2 11H4z" fill="#3a98d8"/></svg>Shop</div>

  <div class="abs sub-site" style="left:420px">Blog<span>blog.zellopak.com</span></div>
  <div class="abs sub-site" style="left:521px">News<span>news.zellopak.com</span></div>
  <div class="abs sub-site" style="left:625px">Events<span>events.zellopak.com</span></div>
  <div class="abs rule" style="left:93px;top:1104px;width:611px"></div>

  <div class="abs cities">Atlanta &nbsp;|&nbsp; Dallas<br>Las Vegas &nbsp;|&nbsp; New York</div>
  <div class="abs promo" style="left:214px;width:134px">TESTIMONIALS
    <svg width="20" height="26" viewBox="0 0 20 26" aria-hidden="true"><rect x="4" y="10" width="12" height="16" rx="3" fill="#5c6670"/><rect x="8" y="12" width="4" height="10" fill="#dfe4e8"/></svg></div>
  <div class="abs promo" style="left:348px;width:113px">ADVERTISE<br>WITH US
    <svg width="22" height="18" viewBox="0 0 22 18" aria-hidden="true"><path d="M2 6h5l9-5v16l-9-5H2z" fill="#dfe4e8"/><rect x="4" y="12" width="3" height="5" fill="#8cc63f"/></svg></div>
  <div class="abs promo" style="left:461px;width:140px">SEND US YOUR<br>FEEDBACK
    <svg width="26" height="20" viewBox="0 0 26 20" aria-hidden="true"><ellipse cx="11" cy="8" rx="10" ry="7" fill="#8cc63f"/><ellipse cx="17" cy="12" rx="8" ry="6" fill="#dfe4e8"/></svg></div>
  <div class="abs" style="left:601px;top:1106px;width:1px;height:50px;background:var(--footer-line)"></div>
  <div class="abs social" style="left:611px;background:#3aa6e0"></div>
  <div class="abs social" style="left:646px;background:#3b5a9a"></div>
  <div class="abs social" style="left:681px;background:#d0211c"></div>
  <div class="abs rule" style="left:93px;top:1156px;width:611px"></div>

  <div class="abs legal">Advertise with Zellopak &nbsp;|&nbsp; About us &nbsp;|&nbsp; Contact us &nbsp;|&nbsp; Privacy Policy &nbsp;|&nbsp; Terms of Service &nbsp;|&nbsp; Careers</div>
  <div class="abs copyright">All rights reserved © 2011 zellopak</div>

</div>
</body>
</html>
```